QuillBackDesk Website Redesign

I'm looking to redesign our website QuillBackDesk.com. The main goal is to give it a fresh design that is easy on the eyes and pushes the users to creating an account.

Our platform is very simple and we only do one thing, we use ai to generate response to customer and product reviews.

See attached file to see the pricing section style.

On the homepage just under the hero section, I would like to include the wording:
"Write replies to the reviews you get on sites like:" then show the logos like we have on our register page: https://app.quillbackdesk.com/public/index.php

Target Market(s)

Business owners with brick and morter business or any business or product that gets online reviews

Industry/Entity Type

reputation management

Number of Pages Required

2 page

Requirements
Must have
• Home page and pricing page

```html
<!DOCTYPE html>
<html lang="en">
<head>
<meta charset="utf-8">
<title>QuillBackDesk – AI replies to your reviews</title>
<link href="https://fonts.googleapis.com/css2?family=Poppins:wght@400;500;600;700&display=swap" rel="stylesheet">
<style>
:root{
  --blue:#1e3f9a;
  --blue-dark:#163283;
  --orange:#fdab00;
  --orange-deep:#fb8c0a;
  --ink:#222;
  --muted:#555;
  --light:#f4f4f4;
  --white:#fff;
}
*{margin:0;padding:0;box-sizing:border-box}
html,body{width:1200px;height:4156px;overflow:hidden}
body{position:relative;font-family:'Poppins',sans-serif;color:var(--ink);background:var(--white)}
.abs{position:absolute}
.brand{display:flex;align-items:center;gap:10px;font-weight:700;font-size:28px;color:var(--blue);letter-spacing:-.5px}
.brand-mark{width:18px;height:18px;border-radius:50%;background:var(--orange)}
.nav a{position:absolute;top:32px;font-size:14px;color:#333;text-decoration:none}
.btn{position:absolute;display:flex;align-items:center;justify-content:center;font-weight:700;color:var(--white);font-size:13px;text-transform:uppercase;letter-spacing:.3px}
.btn-blue{background:var(--blue)}
.btn-orange{background:var(--orange)}
.hero-photo{left:597px;top:90px;width:603px;height:642px;background:linear-gradient(135deg,#2d4a8c 0%,#6a84b8 40%,#c9b8a6 70%,#8a6e5a 100%)}
.hero-accent{left:576px;top:258px;width:40px;height:300px;background:var(--orange);border-radius:30px 0 0 30px}
.hero-title{left:111px;top:276px;width:460px;font-size:46px;line-height:60px;font-weight:700;color:var(--ink)}
.dots span{position:absolute;top:635px;width:11px;height:11px;border-radius:50%;background:#ddd}
.lead{left:0;width:1200px;top:826px;text-align:center;font-size:34px;line-height:43px;font-weight:700}
.feature{position:absolute;top:992px;width:215px}
.feature .art{height:155px;border-radius:12px;background:linear-gradient(135deg,#e6ecfa,#fde6b0)}
.feature h3{margin-top:14px;font-size:16px;line-height:26px;font-weight:700;height:52px}
.feature p{margin-top:16px;font-size:12.5px;line-height:21.5px;color:var(--muted)}
.how{left:0;top:1416px;width:1200px;height:605px;background:var(--blue)}
.how h2{position:absolute;top:96px;width:100%;text-align:center;color:var(--white);font-size:34px;font-weight:700}
.step{position:absolute;top:177px;width:300px;text-align:center;color:var(--white)}
.ring{margin:0 auto;width:160px;height:160px;border-radius:50%;border:3px solid var(--orange);display:flex;align-items:center;justify-content:center;position:relative}
.ring .core{width:136px;height:136px;border-radius:50%;background:var(--white);display:flex;align-items:center;justify-content:center}
.num{position:absolute;bottom:-20px;left:50%;transform:translateX(-50%);width:38px;height:38px;border-radius:50%;background:var(--orange);font-weight:700;font-size:15px;display:flex;align-items:center;justify-content:center}
.step .kicker{margin-top:40px;color:var(--orange);font-size:12px;font-weight:600}
.step h4{margin-top:4px;font-size:17px;font-weight:700}
.step p{margin-top:8px;font-size:12.5px;line-height:21.5px}
.arrow{position:absolute;top:232px}
.pricing-title{left:0;width:1200px;top:2132px;text-align:center;font-size:34px;line-height:43px;font-weight:700}
.pricing-sub{left:0;width:1200px;top:2216px;text-align:center;font-size:16px;color:var(--orange)}
.plan{position:absolute;top:2263px;width:376px;height:466px;color:var(--white);overflow:hidden;text-align:center}
.plan h3{margin-top:48px;font-size:22px;line-height:30px;font-weight:700}
.plan .desc{margin-top:14px;font-size:14px;line-height:26px}
.price{margin:14px auto 0;width:223px;height:41px;display:flex;align-items:center;justify-content:center;gap:6px;font-size:14px}
.price b{font-size:21px}
.plan ul{list-style:none;text-align:left;margin:22px 0 0 76px}
.plan li{font-size:14px;line-height:34px;display:flex;align-items:center;gap:10px}
.tick{width:14px;height:14px;border-radius:50%;display:inline-flex;align-items:center;justify-content:center}
.plan svg.wave{position:absolute;left:0;bottom:0}
.faq-bg{left:0;top:2834px;width:1200px;height:586px;background:var(--light)}
.faq-title{left:111px;top:2928px;font-size:34px;font-weight:700}
.faq-item{position:absolute;left:111px;width:489px;height:56px;border:1px solid #ddd;border-radius:28px;background:var(--white);display:flex;align-items:center;justify-content:space-between;padding:0 18px 0 30px;font-size:14px}
.faq-item i{width:30px;height:30px;border-radius:50%;background:var(--orange);color:var(--white);font-style:normal;display:flex;align-items:center;justify-content:center;font-size:16px}
.faq-photo{left:658px;top:2949px;width:380px;height:380px;border-radius:50%;background:linear-gradient(135deg,#cfd9ea,#9c7a62 60%,#e7e2d6);border-right:20px solid var(--blue)}
.cta{left:0;top:3420px;width:1200px;height:282px;background:linear-gradient(180deg,var(--orange) 0%,var(--orange-deep) 100%);text-align:center;color:var(--white)}
.cta h2{margin-top:62px;font-size:34px;font-weight:700}
.cta p{margin-top:12px;font-size:16px}
.cta .go{margin:18px auto 0;width:144px;height:38px;background:var(--white);color:var(--blue);font-size:13px;font-weight:700;display:flex;align-items:center;justify-content:center}
.contact{position:absolute;top:3870px;width:300px;text-align:center;font-size:13px;line-height:25px;color:#444}
.contact .ic{margin:0 auto 18px;width:70px;height:70px;border-radius:50%;background:var(--blue);border:5px solid #c9d3ee;display:flex;align-items:center;justify-content:center}
.rule{left:111px;top:4033px;width:978px;height:1px;background:#ccc}
.copyright{left:0;width:1200px;top:4057px;text-align:center;font-size:13px;color:#333}
</style>
</head>
<body>

<header>
  <div class="brand abs" style="left:111px;top:28px"><span class="brand-mark"></span>QuillBackDesk</div>
  <nav class="nav">
    <a style="left:395px">Why Reply?</a>
    <a style="left:505px">How It Works</a>
    <a style="left:624px">Pricing</a>
    <a style="left:702px">Blog</a>
    <a style="left:760px">Login</a>
  </nav>
  <div class="btn btn-blue" style="left:834px;top:24px;width:98px;height:36px">Try Free</div>
  <div class="btn btn-orange" style="left:944px;top:24px;width:145px;height:36px">Start for Free</div>
</header>

<section class="hero">
  <div class="hero-accent abs"></div>
  <div class="hero-photo abs" role="img" aria-label="Hand holding a phone with floating star-rating review bubbles"></div>
  <h1 class="hero-title abs">Write replies to the reviews you get on sites like</h1>
  <div class="btn btn-orange" style="left:111px;top:471px;width:144px;height:35px">Start for Free</div>
  <div class="btn btn-blue" style="left:268px;top:471px;width:142px;height:35px">Learn More</div>
  <div class="dots">
    <span style="left:112px;background:var(--orange)"></span>
    <span style="left:131px"></span>
    <span style="left:151px"></span>
    <span style="left:170px"></span>
  </div>
</section>

<section class="benefits">
  <h2 class="lead abs">It's simple. Our tool writes replies and responses<br>to the reviews your customers leave. Doesn't<br>matter if it's 1 or 5 stars.</h2>
  <div class="feature" style="left:110px">
    <div class="art" role="img" aria-label="Illustration of a review card with a reply"></div>
    <h3>Improved SEO</h3>
    <p>MapSeek loves seeing you leave a reply to your reviews and will give you a boost in their search results and local SEO.</p>
  </div>
  <div class="feature" style="left:365px">
    <div class="art" role="img" aria-label="Illustration of a customer review with a business reply"></div>
    <h3>Build Customer Trust</h3>
    <p>Customers want to know there are humans behind your companies product or service. Show them you value their time.</p>
  </div>
  <div class="feature" style="left:621px">
    <div class="art" role="img" aria-label="Illustration of a loyal customer's review card"></div>
    <h3>Increase Customer Loyalty</h3>
    <p>Taking the time to reply to a review shows your customers you care about them and their business. Show them some love!</p>
  </div>
  <div class="feature" style="left:876px">
    <div class="art" role="img" aria-label="Illustration of a new customer reading a review"></div>
    <h3>Convert New Customers</h3>
    <p>FACT: Potential customers read reviews before making a decision. Give a good first impression with personalized replies.</p>
  </div>
</section>

<section class="how abs">
  <h2>How it works</h2>
  <div class="step" style="left:124px">
    <div class="ring"><div class="core">
      <svg width="70" height="70" viewBox="0 0 70 70" fill="none" stroke="#fdab00" stroke-width="3"><circle cx="30" cy="20" r="12"/><path d="M8 58c0-14 10-22 22-22s16 4 19 9"/><circle cx="50" cy="52" r="11"/><path d="M50 46v12M44 52h12"/></svg>
    </div><div class="num">01</div></div>
    <div class="kicker">Create An Account</div>
    <h4>1 minute account creation</h4>
    <p>Gain access to the most powerful tool for writing unique and personal responses to the reviews your customers leave your business.</p>
  </div>
  <svg class="arrow" style="left:388px" width="96" height="40" viewBox="0 0 96 40" fill="none" stroke="#fff" stroke-width="4" stroke-linecap="round"><path d="M4 24C30 4 62 4 86 26"/><path d="M72 28l14-2-2-14"/></svg>
  <div class="step" style="left:450px">
    <div class="ring"><div class="core">
      <svg width="72" height="64" viewBox="0 0 72 64" fill="none" stroke="#fdab00" stroke-width="2.5"><rect x="6" y="4" width="60" height="24" rx="4"/><path d="M16 12l2 4 4 .5-3 3 1 4-4-2-4 2 1-4-3-3 4-.5zM36 12l2 4 4 .5-3 3 1 4-4-2-4 2 1-4-3-3 4-.5zM56 12l2 4 4 .5-3 3 1 4-4-2-4 2 1-4-3-3 4-.5z" stroke-width="1.8"/><circle cx="18" cy="44" r="8"/><path d="M8 60c2-6 6-8 10-8s8 2 10 8"/><path d="M36 40h28M36 48h28M36 56h28"/></svg>
    </div><div class="num">02</div></div>
    <div class="kicker">Copy And Paste The Review</div>
    <h4>We make it way too simple!</h4>
    <p>Just copy the customer review and paste it into your account dashboard.</p>
  </div>
  <svg class="arrow" style="left:712px" width="96" height="40" viewBox="0 0 96 40" fill="none" stroke="#fff" stroke-width="4" stroke-linecap="round"><path d="M4 24C30 4 62 4 86 26"/><path d="M72 28l14-2-2-14"/></svg>
  <div class="step" style="left:776px">
    <div class="ring"><div class="core">
      <svg width="70" height="66" viewBox="0 0 70 66" fill="none" stroke="#fdab00" stroke-width="2.5"><circle cx="22" cy="20" r="9"/><circle cx="22" cy="20" r="3"/><path d="M22 6v4M22 30v4M8 20h4M32 20h4"/><circle cx="44" cy="12" r="6"/><path d="M6 58l10-10c4-3 10-3 14 0h14c3 0 3 5 0 5H32"/><path d="M30 53l18-4 12-8c3-2 6 2 3 4L48 58H20"/><path d="M46 30l4 4 8-9"/></svg>
    </div><div class="num">03</div></div>
    <div class="kicker">Personalized Response In Seconds</div>
    <h4>Only a 10 second wait</h4>
    <p>In just seconds you'll receive 3 unique and personal responses. Choose the reply you like best or tell our system to generate 3 more.</p>
  </div>
</section>

<section class="pricing">
  <h2 class="pricing-title abs">Never worry about having to come up with a<br>unique response to each review ever again!</h2>
  <p class="pricing-sub abs">If your business, product or service receives reviews, this tool will save you hundreds of hours.</p>

  <div class="plan" style="left:215px;background:var(--blue)">
    <h3>Monthly<br>Subscriptions</h3>
    <p class="desc">Perfect for getting started for<br>one business/product</p>
    <div class="price" style="background:var(--orange)">Starts at <b>$9.99</b> / month</div>
    <ul>
      <li><span class="tick" style="background:var(--orange)"><svg width="8" height="8" viewBox="0 0 8 8"><path d="M1 4l2 2 4-4" stroke="#fff" stroke-width="1.6" fill="none"/></svg></span>Personalized responses</li>
      <li><span class="tick" style="background:var(--orange)"><svg width="8" height="8" viewBox="0 0 8 8"><path d="M1 4l2 2 4-4" stroke="#fff" stroke-width="1.6" fill="none"/></svg></span>30+ Languages</li>
      <li><span class="tick" style="background:var(--orange)"><svg width="8" height="8" viewBox="0 0 8 8"><path d="M1 4l2 2 4-4" stroke="#fff" stroke-width="1.6" fill="none"/></svg></span>Auto-Save</li>
      <li><span class="tick" style="background:var(--orange)"><svg width="8" height="8" viewBox="0 0 8 8"><path d="M1 4l2 2 4-4" stroke="#fff" stroke-width="1.6" fill="none"/></svg></span>Revision History</li>
      <li><span class="tick" style="background:var(--orange)"><svg width="8" height="8" viewBox="0 0 8 8"><path d="M1 4l2 2 4-4" stroke="#fff" stroke-width="1.6" fill="none"/></svg></span>Assign members usage limits</li>
    </ul>
    <svg class="wave" width="376" height="50" viewBox="0 0 376 50" preserveAspectRatio="none"><path d="M0 20C90 0 200 8 376 26V50H0z" fill="#fdab00"/></svg>
  </div>

  <div class="plan" style="left:606px;background:var(--orange)">
    <h3>Agency<br>Subscriptions</h3>
    <p class="desc">Perfect for multiple<br>clients/products per month</p>
    <div class="price" style="background:var(--blue)">Starts at <b>$75.00</b>/ month</div>
    <ul>
      <li><span class="tick" style="background:var(--blue)"><svg width="8" height="8" viewBox="0 0 8 8"><path d="M1 4l2 2 4-4" stroke="#fff" stroke-width="1.6" fill="none"/></svg></span>Everything in the Startup plan</li>
      <li><span class="tick" style="background:var(--blue)"><svg width="8" height="8" viewBox="0 0 8 8"><path d="M1 4l2 2 4-4" stroke="#fff" stroke-width="1.6" fill="none"/></svg></span>Dedicated Account Manager</li>
      <li><span class="tick" style="background:var(--blue)"><svg width="8" height="8" viewBox="0 0 8 8"><path d="M1 4l2 2 4-4" stroke="#fff" stroke-width="1.6" fill="none"/></svg></span>Onboarding &amp; Training</li>
      <li><span class="tick" style="background:var(--blue)"><svg width="8" height="8" viewBox="0 0 8 8"><path d="M1 4l2 2 4-4" stroke="#fff" stroke-width="1.6" fill="none"/></svg></span>Unlimited Integrations</li>
    </ul>
    <svg class="wave" width="376" height="50" viewBox="0 0 376 50" preserveAspectRatio="none"><path d="M0 20C90 0 200 8 376 26V50H0z" fill="#1e3f9a"/></svg>
  </div>
</section>

<section class="faq">
  <div class="faq-bg abs"></div>
  <h2 class="faq-title abs">Frequently Asked Questions</h2>
  <div class="faq-item" style="top:3010px">Why is it important to respond to MapSeek reviews?<i>+</i></div>
  <div class="faq-item" style="top:3094px">Why is it important to respond to negative reviews?<i>+</i></div>
  <div class="faq-item" style="top:3176px">How can I trust someone who doesn't work at my<i>+</i></div>
  <div class="faq-item" style="top:3260px">Which online review sites does QuillBackDesk.com<i>+</i></div>
  <div class="faq-photo abs" role="img" aria-label="Photo of a smiling businesswoman reading documents at her desk"></div>
</section>

<section class="cta abs">
  <h2>Ready to give QuillBackDesk a try?</h2>
  <p>Get started today with one FREE Reply to your Review. No credit card required.</p>
  <div class="go">TRY FOR FREE</div>
</section>

<footer>
  <div class="brand abs" style="left:0;width:1200px;justify-content:center;top:3788px"><span class="brand-mark"></span>QuillBackDesk</div>
  <div class="contact" style="left:177px">
    <div class="ic"><svg width="22" height="26" viewBox="0 0 22 26"><path d="M11 1C5.5 1 2 5 2 10c0 7 9 15 9 15s9-8 9-15c0-5-3.5-9-9-9z" fill="#fff"/><circle cx="11" cy="10" r="3.5" fill="#1e3f9a"/></svg></div>
    123,Lorem ipsum dolor sit<br>amet, conse
  </div>
  <div class="contact" style="left:450px">
    <div class="ic"><svg width="24" height="18" viewBox="0 0 24 18"><rect x="1" y="1" width="22" height="16" rx="2" fill="#fff"/><path d="M2 3l10 7 10-7" stroke="#1e3f9a" stroke-width="2" fill="none"/></svg></div>
    hello@quillbackdesk.com
  </div>
  <div class="contact" style="left:723px">
    <div class="ic"><svg width="22" height="22" viewBox="0 0 22 22"><path d="M5 1l4 5-2 3c1 3 3 5 6 6l3-2 5 4-2 4C10 21 1 12 1 3z" fill="#fff"/></svg></div>
    +1 888 888 8888
  </div>
  <div class="rule abs"></div>
  <p class="copyright abs">© Copyright 2023 All Rights Reserved | Terms and Conditions</p>
</footer>

</body>
</html>
```